Blue Harbor Trophies & Awards Unique Business Card Design

Recently selected a new logo design and waiting to recieve print files. I've attached image for your review. We are a trophies and awards company that provides engraving on trophies, plaques, name plates, name tags, desk sets, medals, acrylics, and signage.

We are located in Monroe, Louisiana and provide this service with computerized & laser engraving equipment.

Target Market(s)

Corporate, Sport, Church, and Special Events

Industry/Entity Type

Business

Contact Information for Business Card

I'd like to see the following list on the card: Trophies, Plaques, Name Plates, Name Tags, Desk Sets, Medals, Certificates... this is accomplished with Computerized & Laser Engraving

Colors
0555a3
ec1f27
ffffff

Requirements
Must have
• I like either single or double sided. If a design can be created with a frosted card stock I'd consider single. Must be Red, White, and Blue. Dale Penrow - Owner, 415 W 9th Ave, Monroe, La 70384 office 318-555-2190 fax 318-555-2186 email: blueharbor@blueharbortrophyco.example, and website: www.blueharbortrophyco.example

```html
<!DOCTYPE html>
<html lang="en">
<head>
<meta charset="utf-8">
<title>Blue Harbor Trophies &amp; Awards – Business Card</title>
<link rel="stylesheet" href="https://fonts.googleapis.com/css2?family=Arimo:wght@400;700&family=Tinos&display=swap">
<style>
  :root {
    --brand-blue: #0555a3;
    --brand-red: #ec1f27;
    --card-white: #ffffff;
    --backdrop: #160909;
    --serif: "Tinos", "Times New Roman", serif;
    --sans: "Arimo", Arial, sans-serif;
  }
  * { margin: 0; padding: 0; box-sizing: border-box; }
  html, body {
    width: 1200px;
    height: 673px;
    overflow: hidden;
    background: var(--backdrop);
  }
  .canvas {
    position: relative;
    width: 1200px;
    height: 673px;
  }
  .business-card {
    position: absolute;
    left: 180px;
    top: 96px;
    width: 840px;
    height: 480px;
    background: var(--card-white);
    overflow: hidden;
  }
  .card-bands {
    position: absolute;
    inset: 0;
    width: 840px;
    height: 480px;
  }
  .band-blue { fill: var(--brand-blue); }
  .band-red { fill: var(--brand-red); }

  .contact-panel {
    position: absolute;
    left: 0;
    top: 0;
    width: 340px;
    height: 480px;
    color: var(--card-white);
  }
  .owner-name {
    position: absolute;
    left: 0;
    width: 340px;
    top: 76px;
    text-align: center;
    font-family: var(--serif);
    font-size: 26px;
    line-height: 1;
  }
  .owner-rule {
    position: absolute;
    left: 109px;
    top: 110px;
    width: 122px;
    height: 1.5px;
    background: var(--card-white);
  }
  .owner-title {
    position: absolute;
    left: 0;
    width: 340px;
    top: 116px;
    text-align: center;
    font-family: var(--serif);
    font-size: 25px;
    line-height: 1;
  }
  .address,
  .phones {
    position: absolute;
    left: 80px;
    font-family: var(--sans);
    font-size: 18px;
    line-height: 28px;
  }
  .address { top: 166px; }
  .phones { top: 250px; left: 86px; }
  .web-contact {
    position: absolute;
    left: 50px;
    top: 330px;
    width: 290px;
    font-family: var(--serif);
    font-size: 15.5px;
    line-height: 24px;
    white-space: nowrap;
  }

  .brand-lockup {
    position: absolute;
    left: 440px;
    top: 172px;
    width: 390px;
    display: flex;
    align-items: center;
    gap: 14px;
  }
  .brand-dot {
    flex: none;
    width: 30px;
    height: 30px;
    border-radius: 50%;
    background: var(--brand-red);
  }
  .brand-name {
    font-family: var(--sans);
    font-weight: 700;
    font-size: 34px;
    line-height: 1.15;
    color: var(--brand-blue);
    white-space: nowrap;
  }
  .services {
    position: absolute;
    left: 440px;
    top: 300px;
    width: 370px;
    font-family: var(--sans);
    font-size: 14px;
    line-height: 21px;
    color: var(--brand-blue);
  }
  .services-note {
    color: var(--brand-red);
  }
</style>
</head>
<body>
<main class="canvas">
  <section class="business-card" aria-label="Blue Harbor Trophies &amp; Awards business card">
    <svg class="card-bands" viewBox="0 0 840 480" aria-hidden="true">
      <polygon class="band-blue" points="0,0 362,0 346,480 0,480"/>
      <polygon class="band-red" points="362,0 424,0 362,480 346,480"/>
    </svg>

    <div class="contact-panel">
      <p class="owner-name">Dale Penrow</p>
      <span class="owner-rule"></span>
      <p class="owner-title">Owner</p>
      <p class="address">415 W 9th Ave, Monroe,<br>La 70384</p>
      <p class="phones">Office 318-555-2190<br>Fax 318-555-2186</p>
      <p class="web-contact">blueharbor@blueharbortrophyco.example<br>www.blueharbortrophyco.example</p>
    </div>

    <div class="brand-lockup">
      <span class="brand-dot" aria-hidden="true"></span>
      <p class="brand-name">Blue Harbor<br>Trophies &amp; Awards</p>
    </div>

    <p class="services">Trophies · Plaques · Name Plates · Name Tags<br>Desk Sets · Medals · Certificates<br><span class="services-note">Computerized &amp; Laser Engraving</span></p>
  </section>
</main>
</body>
</html>
```